Hair Extension Aftercare sheet

This sheet is to give to customers regarding the aftercare of hair extensions. There should be Simple and minimal look - approx A5 size and can be folded to suit. I have attached the content and logo files for use.
We are not looking for to much artwork just clean, professional look.
All the content provided in a compact flyer format i.e
A foldable A5 pamphlet or the like, this is for packaging requirements
Please do not submit A4 layouts

Industry/Entity Type

Hair And Beauty

Requirements
Must have
• All the content provided in a compact flyer format i.e
• A foldable A5 pamphlet or the like, this is for packaging requirements
Should not have
• tacky art work or images - must be clean lines

```html
<!DOCTYPE html>
<html lang="en">
<head>
<meta charset="utf-8">
<title>Elena Marsh Hair Extensions – Aftercare Pamphlet</title>
<link href="https://fonts.googleapis.com/css2?family=Lato:wght@400;700;900&display=swap" rel="stylesheet">
<style>
  :root{
    --gold:#eeb021;
    --gold-deep:#d99a12;
    --gold-text:#c8901a;
    --ink:#1f1a17;
    --maroon:#3a1216;
    --paper-light:#f4f4f4;
    --paper-mid:#d8d8d8;
    --stage:#e4e4e4;
  }
  *{box-sizing:border-box;margin:0;padding:0}
  html,body{width:1200px;height:848px;overflow:hidden}
  body{background:var(--stage);font-family:"Lato",sans-serif;color:var(--ink);position:relative}
  .page{position:absolute;top:28px;width:560px;height:792px;overflow:hidden;
    background:linear-gradient(90deg,var(--paper-mid),var(--paper-light) 55%,#ffffff);}
  .page--inside{left:40px}
  .page--cover{left:600px;background:linear-gradient(90deg,#cfcfcf,#f2f2f2 45%,#ffffff)}
  .page svg.shapes{position:absolute;inset:0}

  /* inside page */
  .aftercare{position:absolute;left:34px;top:232px;width:492px}
  .aftercare h2{font-weight:900;font-size:19px;letter-spacing:.5px;margin-bottom:7px}
  .aftercare ul{list-style:none}
  .aftercare li{position:relative;padding-left:16px;font-size:12.3px;line-height:1.4;margin-bottom:4px}
  .aftercare li::before{content:"";position:absolute;left:2px;top:6px;width:6px;height:6px;border-radius:50%;background:var(--gold-deep)}
  .gallery{position:absolute;left:30px;top:468px;width:500px;height:150px;
    border:5px solid var(--gold-deep);display:flex;gap:4px;background:var(--gold-deep)}
  .gallery .photo{flex:1}
  .contact{position:absolute;left:34px;top:660px}
  .contact h2{font-weight:900;font-size:19px;margin-bottom:10px}
  .contact ul{list-style:none}
  .contact li{display:flex;align-items:center;gap:10px;font-size:12.5px;margin-bottom:9px}
  .contact .dot{width:18px;height:18px;border-radius:50%;background:#2f4a8a;flex:none}
  .contact .dot--alt{background:#b23a6a}
  .direct{position:absolute;left:300px;top:700px}
  .direct li{display:flex;align-items:center;gap:10px;font-size:12.5px;margin-bottom:12px;list-style:none}

  /* cover page */
  .brand{position:absolute;left:0;right:0;top:412px;text-align:center}
  .brand__name{font-weight:400;font-size:34px;letter-spacing:9px;color:var(--ink)}
  .brand__sub{font-weight:400;font-size:12px;letter-spacing:7px;color:#555;margin-top:2px}
  .tagline{position:absolute;left:0;right:0;top:500px;text-align:center}
  .tagline__lead{font-size:22px;font-weight:400;color:#2a2320}
  .tagline__main{font-size:38px;font-weight:900;color:var(--gold-text);margin-top:2px}
  .tagline__tail{font-size:23px;font-weight:700;color:#2a2320;margin-top:2px}
  .web{position:absolute;left:0;right:0;top:660px;text-align:center;font-weight:700;font-size:14px;color:var(--ink)}
</style>
</head>
<body>

<section class="page page--inside">
  <svg class="shapes" width="560" height="792" viewBox="0 0 560 792">
    <defs>
      <linearGradient id="photoTop" x1="0" y1="0" x2="1" y2="0">
        <stop offset="0" stop-color="#e8e2dc"/><stop offset=".5" stop-color="#c79a80"/><stop offset="1" stop-color="#f1ece8"/>
      </linearGradient>
    </defs>
    <path d="M0 0H560V150C440 170 260 160 0 215Z" fill="url(#photoTop)" role="img" aria-label="Photo of a smiling woman with long brown hair"/>
    <path d="M0 215C260 160 440 170 560 150V162C440 184 260 178 0 235Z" fill="var(--gold)"/>
    <path d="M0 650C200 640 380 612 560 575V792H0Z" fill="var(--gold)"/>
  </svg>

  <div class="aftercare">
    <h2>AFTERCARE</h2>
    <ul>
      <li>Brush your extensions gently twice a day with a soft bristle brush, starting at the ends and working up.</li>
      <li>Wash with sulphate-free shampoo and conditioner, keeping conditioner away from the bonds.</li>
      <li>Never sleep with wet hair. Dry fully and tie it in a loose braid or ponytail at night.</li>
      <li>Use a heat protector and keep tools below 180°C, away from the attachment points.</li>
      <li>Avoid chlorine and salt water, or rinse straight after swimming.</li>
      <li>Book a maintenance appointment every 6–8 weeks to keep your hair natural and long lasting.</li>
    </ul>
  </div>

  <div class="gallery">
    <div class="photo" role="img" aria-label="Before photo of dark wavy hair" style="background:linear-gradient(#3b2a2e,#1c1416)"></div>
    <div class="photo" role="img" aria-label="After photo of long dark curls" style="background:linear-gradient(#4a3336,#221719)"></div>
    <div class="photo" role="img" aria-label="Long blonde curled hair" style="background:linear-gradient(#e8d4a8,#b58e5a)"></div>
    <div class="photo" role="img" aria-label="Client with blonde extensions and sunglasses" style="background:linear-gradient(#cbb89a,#7a6a58)"></div>
    <div class="photo" role="img" aria-label="Client with blonde extensions wearing a hat" style="background:linear-gradient(#a99c86,#6e6352)"></div>
  </div>

  <div class="contact">
    <h2>CONTACT US</h2>
    <ul>
      <li><span class="dot"></span>Elena-Marsh-Hair-Extensions</li>
      <li><span class="dot dot--alt"></span>elenamarshhairextensions</li>
    </ul>
  </div>
  <ul class="direct">
    <li>
      <svg width="18" height="18" viewBox="0 0 24 24"><circle cx="12" cy="12" r="10.5" fill="none" stroke="#1f1a17" stroke-width="1.6"/><path d="M8.5 7c.6-.4 1.2-.3 1.5.2l1 1.7c.3.5.1 1-.3 1.3l-.6.4c.5 1.2 1.5 2.2 2.7 2.8l.4-.6c.3-.4.9-.6 1.3-.3l1.7 1c.5.3.6.9.2 1.5-.8 1.1-2 1.3-3.2.7-2.4-1.200-4.200-3-5.300-5.400-.5-1.200-.3-2.400.6-3.300z" fill="#1f1a17"/></svg>
      61400123456
    </li>
    <li>
      <svg width="20" height="14" viewBox="0 0 20 14"><rect x="1" y="1" width="18" height="12" fill="none" stroke="#1f1a17" stroke-width="1.8"/><path d="M1 1l9 7 9-7" fill="none" stroke="#1f1a17" stroke-width="1.8"/></svg>
      info@elenamarsh.com
    </li>
  </ul>
</section>

<section class="page page--cover">
  <svg class="shapes" width="560" height="792" viewBox="0 0 560 792">
    <defs>
      <radialGradient id="coverPhoto" cx=".6" cy=".4" r=".7">
        <stop offset="0" stop-color="#c0552a"/><stop offset=".45" stop-color="#7a2a1e"/><stop offset="1" stop-color="#3a1216"/>
      </radialGradient>
    </defs>
    <path d="M0 0H560V300C420 300 260 330 0 370Z" fill="url(#coverPhoto)" role="img" aria-label="Portrait of a woman with voluminous red curly hair"/>
    <path d="M0 370C260 330 420 300 560 300V320C420 318 260 350 0 384Z" fill="var(--gold)"/>
    <path d="M0 740C200 732 400 712 560 675V792H0Z" fill="var(--gold)"/>
  </svg>

  <div class="brand">
    <div class="brand__name">ELENA MARSH</div>
    <div class="brand__sub">HAIR EXTENSIONS</div>
  </div>
  <div class="tagline">
    <div class="tagline__lead">Our Philosophy Is Simple</div>
    <div class="tagline__main">To Provide High Quality</div>
    <div class="tagline__tail">Long lasting Hair Extensions</div>
  </div>
  <div class="web">www.elenamarsh.com</div>
</section>

</body>
</html>
```